Catering company needs business cards

We need new business cards for growing catering company.

Industry/Entity Type

Business

Requirements
Must have
• Company logo
• Marisol Quedenfeldt
• Catering Director
• marisol.t.quedenfeldt-1@orvanta-mail.org
• 407-555-0182
• 407-555-0267
• Building R2-718 PTX
• Brightwater Launch Campus
• Florida, 33741

```html
<!DOCTYPE html>
<html lang="en">
<head>
<meta charset="utf-8">
<title>Clearwater Catering – Business Cards</title>
<link rel="stylesheet" href="https://fonts.googleapis.com/css2?family=Didact+Gothic&display=swap">
<style>
  :root {
    --backdrop: #ebe8e3;
    --card: #ffffff;
    --sky-blue: #1f9ae0;
    --brand-blue: #1b6fb8;
    --ink: #2b2b2b;
    --muted: #555555;
    --icon: #4a4a4a;
  }
  * { margin: 0; padding: 0; box-sizing: border-box; }
  html, body {
    width: 1200px; height: 1000px; overflow: hidden;
    background: var(--backdrop);
  }
  .canvas { position: relative; width: 1200px; height: 1000px; }

  .card {
    position: absolute;
    left: 210px;
    width: 780px;
    height: 430px;
    background: var(--card);
    box-shadow: 0 6px 18px rgba(0,0,0,0.12);
    overflow: hidden;
    font-family: "Didact Gothic", sans-serif;
  }
  .card--front { top: 40px; border-radius: 56px 0 56px 0; }
  .card--back  { top: 520px; border-radius: 0 0 64px 0; }

  .accent-bar {
    position: absolute; right: 0; top: 0;
    width: 18px; height: 210px;
    background: var(--sky-blue);
  }

  .name-band {
    position: absolute; left: 0; top: 120px;
    width: 300px; height: 46px;
    background: var(--sky-blue);
    color: #fff;
    font-size: 26px; line-height: 46px;
    padding-left: 16px;
    white-space: nowrap;
  }
  .job-title {
    position: absolute; left: 0; top: 172px; width: 300px;
    text-align: right;
    font-size: 14px; color: var(--muted);
  }

  .wordmark {
    position: absolute;
    color: var(--brand-blue);
    font-weight: 400;
    white-space: nowrap;
    text-align: center;
  }
  .card--front .wordmark { left: 330px; top: 150px; width: 400px; font-size: 24px; }
  .card--back .wordmark { left: 0; top: 190px; width: 780px; font-size: 42px; }

  .contact {
    position: absolute; right: 36px; top: 232px;
    list-style: none;
    font-size: 14px; letter-spacing: 1.5px;
    color: var(--ink);
    text-align: right;
  }
  .contact li {
    display: flex; justify-content: flex-end; align-items: center;
    gap: 8px; height: 26px; white-space: nowrap;
  }
  .contact svg { width: 16px; height: 16px; flex: none; }
  .contact .icon-gap { width: 16px; flex: none; }
</style>
</head>
<body>
<main class="canvas">

  <section class="card card--front" aria-label="Business card front">
    <div class="accent-bar"></div>
    <div class="name-band">Marisol Quedenfeldt</div>
    <div class="job-title">Catering Director</div>

    <div class="wordmark">The Clearwater Catering Company</div>

    <ul class="contact">
      <li>407-555-0182
        <svg viewBox="0 0 16 16" aria-hidden="true"><circle cx="8" cy="8" r="8" fill="var(--icon)"/><rect x="5.5" y="3.5" width="5" height="9" rx="1" fill="none" stroke="#fff" stroke-width="1.2"/></svg>
      </li>
      <li>407-555-0267
        <svg viewBox="0 0 16 16" aria-hidden="true"><circle cx="8" cy="8" r="8" fill="var(--icon)"/><rect x="5.5" y="3.5" width="5" height="9" rx="1" fill="none" stroke="#fff" stroke-width="1.2"/></svg>
      </li>
      <li>marisol.t.quedenfeldt-1@orvanta-mail.org
        <svg viewBox="0 0 16 16" aria-hidden="true"><circle cx="8" cy="8" r="8" fill="var(--icon)"/><circle cx="8" cy="8" r="2" fill="none" stroke="#fff" stroke-width="1.2"/><path d="M10 6v3a1.3 1.3 0 0 0 2.4 0V8a4.4 4.4 0 1 0-1.8 3.6" fill="none" stroke="#fff" stroke-width="1.2"/></svg>
      </li>
      <li>Building R2-718 PTX
        <svg viewBox="0 0 16 16" aria-hidden="true"><circle cx="8" cy="8" r="8" fill="var(--icon)"/><path d="M8 12.5s-3-3.2-3-5.5a3 3 0 0 1 6 0c0 2.3-3 5.5-3 5.5z" fill="none" stroke="#fff" stroke-width="1.1"/><circle cx="8" cy="7" r="1" fill="#fff"/></svg>
      </li>
      <li>Brightwater Launch Campus<span class="icon-gap"></span></li>
      <li>Florida, 33741<span class="icon-gap"></span></li>
    </ul>
  </section>

  <section class="card card--back" aria-label="Business card back">
    <div class="wordmark">The Clearwater Catering Company</div>
  </section>

</main>
</body>
</html>
```